Newsletter Design Project

I need a new design for a monthly newsletter that I do for Marbury Lane Open College Ipswich. I have been doing the same thing since 2009. We are based in Brisbane and we run classes for semi retired and retired people. I write about social activities, class activities, vacancies etc. I take photos and include them we hhave a logo that I always use. and would just like the newsletter to look different and fresh. The logo is Blue

```html
<!DOCTYPE html>
<html lang="en">
<head>
<meta charset="utf-8">
<title>MLOC E Newsletter – June 2013</title>
<link href="https://fonts.googleapis.com/css2?family=Arimo:wght@400;700&family=Righteous&family=PT+Sans:wght@700&display=swap" rel="stylesheet">
<style>
  :root {
    --brand-blue: #2f97d6;
    --heading-blue: #1d8ed6;
    --ink: #1e1e1e;
    --paper: #ffffff;
    --photo-dark: #4f6f8e;
    --photo-light: #c9d6e2;
    --frame-green: #3a9a3a;
  }
  * { margin: 0; padding: 0; box-sizing: border-box; }
  html, body { width: 864px; height: 1200px; overflow: hidden; background: var(--paper); }
  .page { position: relative; width: 864px; height: 1200px; font-family: "Arimo", Arial, sans-serif; color: var(--ink); }

  .masthead-photo {
    position: absolute; left: 0; top: 0; width: 864px; height: 185px;
    background: linear-gradient(90deg, var(--photo-dark) 0%, #7f9bb6 30%, #a9bccd 50%, #6e8cab 70%, var(--photo-light) 100%);
  }
  .masthead-logo {
    position: absolute; left: 533px; top: 55px; width: 148px; height: 76px;
    background: var(--paper); display: flex; align-items: center; justify-content: center; gap: 8px;
  }
  .masthead-logo .mark { width: 14px; height: 14px; background: var(--brand-blue); }
  .masthead-logo .name { font-weight: 700; font-size: 30px; color: var(--brand-blue); }
  .masthead-issue {
    position: absolute; left: 693px; top: 45px; color: var(--paper);
    font-weight: 700; font-size: 16px; line-height: 28px;
  }

  .notice-bar {
    position: absolute; left: 0; top: 185px; width: 864px; height: 53px; background: var(--brand-blue);
    color: var(--paper); font-family: "PT Sans", Arial, sans-serif; font-weight: 700; font-size: 17.5px;
    display: flex; align-items: center; justify-content: center;
  }

  .column { position: absolute; top: 264px; font-size: 16.5px; line-height: 20px; hyphens: auto; -webkit-hyphens: auto; }
  .column-left { left: 62px; width: 348px; }
  .column-right { left: 442px; width: 366px; top: 262px; }
  .column p { margin-bottom: 10px; }
  .section-title {
    font-family: "Righteous", "Arial Rounded MT Bold", sans-serif; font-weight: 400; font-size: 19px;
    line-height: 22px; color: var(--heading-blue); padding-left: 13px; margin: 0 0 12px;
    hyphens: none; -webkit-hyphens: none;
  }
  .column p + .section-title { margin-top: 4px; }
  .promo { color: var(--heading-blue); font-weight: 700; text-transform: uppercase; font-size: 16px; }
  .link { font-weight: 700; }

  .walk-photo {
    position: absolute; left: 486px; top: 926px; width: 268px; height: 200px;
    border: 2px solid var(--frame-green);
    background: linear-gradient(180deg, #7a8f5c 0%, #9fae7a 45%, #b9a98a 100%);
  }

  .footer-bar {
    position: absolute; left: 0; top: 1163px; width: 864px; height: 37px; background: var(--brand-blue);
    color: var(--paper); font-size: 11px; font-weight: 700;
  }
  .footer-bar span { position: absolute; top: 11px; }
  .footer-title { left: 256px; }
  .footer-page { left: 422px; }
  .footer-issue { left: 538px; }
</style>
</head>
<body>
<div class="page">
  <div class="masthead-photo" role="img" aria-label="Blue-toned photo collage of members in a classroom, a building foyer and a computer lab"></div>
  <div class="masthead-logo"><span class="mark"></span><span class="name">MLOC</span></div>
  <div class="masthead-issue">E Newsletter<br>June 2013</div>

  <div class="notice-bar">Please Note: The term 3 Class Schedule will be posted and available online on Monday 17th June</div>

  <div class="column column-left">
    <h2 class="section-title">Winter School 2013: from Clare<br>Hadley</h2>
    <p>Winter is upon us and the Winter School program is complete and up on the website. If you haven’t already done so, it is time to make your selections for this year. Registering couldn’t be simpler Go to the website www.marburylane.org.au - click on the link - type in your name and membership number and tick the boxes. No need to log in. Your email confirmation will be back in no time.</p>
    <p>We have a great program this year with a raft of outside presenters including Peter Garvey who is our Keynote speaker. There are plenty of interesting topics to choose from and include a selection of medical related subjects, history, literature, art, computers and a number of others.</p>
    <p class="promo">Only $5 per session – hurry… don’t miss out !</p>
    <p>NB: Two of the sessions are long and priced at $10.</p>
    <h2 class="section-title">Logan News: from Joan<br>Whitby</h2>
    <p>There will be two brand new classes in Term 3: World Economics with Martin Ellis and Hypnosis for Relaxation, both of which sound very interesting. You can access Ruth Calloway’s blog to read more about her class at <span class="link">www.calmwithruth.com</span>. Also, Neil Brockway will be starting a new Easy Cartooning class.</p>
    <p>Sadly, Ron Halvey, the computer tutor who has given much time and energy to MLOC in Beenleigh and the City is retiring due to family commitments. Ron introduced many members to PCs in the very early years in Fortitude Valley, then Carrington House and Beenleigh over 18 years. As well as teaching, Ron maintained and rebuilt MLOC computer equipment during</p>
  </div>

  <div class="column column-right">
    <p>that time, notably after the computers in Beenleigh were stolen. Past students owe a debt of gratitude to Ron, and his contribution will be sadly missed.</p>
    <p>Most Logan classes continue as in Term 2 and new enrolments will be particularly welcomed in the Beenleigh Book Discussion Group, Cryptic Crosswords, English Country Dancing (great fun!) and Classic Drama and its World. The Travellers Group started in Term 2 is going well, and will be given a longer timeslot in Term 3, as will the Camera Club Group.</p>
    <p>The Logan Committee wish all members a happy holiday and a pleasant and productive time in Term 3.</p>
    <h2 class="section-title">Northside News: from Sue<br>Pemberton</h2>
    <p>New for Term 3 is a Movie Group, meeting once a month at Harbourside for lunch or a snack prior to the movie. There will be a Book Club which will be meeting once a month at Chermside and a talk once a week on “Speeches that Changed The World”.</p>
    <p>We have an amazing walking group run by Maureen Farley every Thursday at 7:30am and it will be continuing into the 3rd term. Besides the walk, they have a lovely morning tea and always check the history of the area and different buildings on their walks.</p>
  </div>

  <div class="walk-photo" role="img" aria-label="Photo of the walking group standing beside a nature reserve sign among bush trees"></div>

  <div class="footer-bar">
    <span class="footer-title">MLOC E-newsletter</span>
    <span class="footer-page">1</span>
    <span class="footer-issue">Issue 6/2013</span>
  </div>
</div>
</body>
</html>
```